PaceUp

This app is built around three game modes—Quick Focus, Daily, and Calming—each offering short, low-stress interactions designed to prime focus, train cognitive skills, or regulate anxiety using neuroscience-informed mechanics. Gameplay spans spatial puzzles, word and memory challenges, and breathing or sensory experiences, all delivered in 1–5 minute routines with clean, calming UI patterns (grids, cards, breathing rings, soft animations). The goal is a cohesive system of micro-games and guided routines that enhance executive function, emotional regulation, and readiness before, during, or after high-stakes moments.

Colors
FFC000
F8CF3A
FAE287
FDF2CF
FEFAEE
F0912C
F2A743
F7CA91
FBE8D2
FDF5EE
EE7325
F08F49
F5BC92
FAE3D3
FDF4ED

```html
<!DOCTYPE html>
<html lang="en">
<head>
<meta charset="utf-8">
<title>PaceUp – Home</title>
<link rel="stylesheet" href="https://fonts.googleapis.com/css2?family=Outfit:wght@300;400;600;700&display=swap">
<style>
  :root {
    --bg: #F5ECE2;
    --band: #F6E8C3;
    --band-soft: #F8EDCB;
    --ink: #3A2A12;
    --ink-soft: #4A3A22;
    --card: #FFFFFF;
    --accent-yellow: #FFC000;
    --orange-top: #F7A869;
    --orange-bottom: #EE7325;
    --yellow-top: #FAE287;
    --yellow-bottom: #FFC000;
    --calm-top: #F5BC92;
    --calm-bottom: #EE5420;
    --nav-icon: #4A3A22;
  }
  * { box-sizing: border-box; margin: 0; padding: 0; }
  html, body { width: 677px; height: 1200px; overflow: hidden; }
  body {
    font-family: "Outfit", sans-serif;
    color: var(--ink);
    background: var(--bg);
    position: relative;
  }
  .backdrop { position: absolute; inset: 0; z-index: 0; }
  .status-bar {
    position: absolute; top: 0; left: 0; right: 0; height: 70px;
    display: flex; justify-content: space-between; align-items: center;
    padding: 0 44px 0 52px; z-index: 2;
  }
  .status-time { font-weight: 600; font-size: 24px; color: #111; }
  .status-icons { display: flex; gap: 8px; align-items: center; }
  .app-header { position: absolute; top: 128px; left: 0; right: 0; text-align: center; z-index: 2; }
  .app-title { font-weight: 600; font-size: 62px; letter-spacing: 0.5px; line-height: 1; }
  .app-tagline { font-weight: 400; font-size: 25px; margin-top: 24px; color: var(--ink-soft); }
  .mode-list {
    position: absolute; top: 300px; left: 34px; right: 34px;
    display: flex; flex-direction: column; gap: 28px; z-index: 2;
  }
  .mode-card {
    height: 212px; background: var(--card); border-radius: 44px;
    display: flex; align-items: center; padding: 0 46px 0 48px;
    box-shadow: 0 22px 34px rgba(120, 95, 60, 0.14);
    border: 1.5px solid transparent;
  }
  .mode-card--active { border-color: var(--accent-yellow); }
  .mode-icon {
    width: 132px; height: 132px; border-radius: 30px; flex: none;
    display: flex; align-items: center; justify-content: center;
  }
  .mode-icon--focus { background: linear-gradient(160deg, var(--orange-top), var(--orange-bottom)); }
  .mode-icon--routine { background: linear-gradient(160deg, var(--yellow-top), var(--yellow-bottom)); }
  .mode-icon--calm { background: linear-gradient(160deg, var(--calm-top), var(--calm-bottom)); }
  .mode-text { flex: 1; margin-left: 30px; }
  .mode-name { font-weight: 600; font-size: 36px; line-height: 1.1; }
  .mode-detail { font-weight: 300; font-size: 22px; margin-top: 12px; color: var(--ink-soft); }
  .mode-chevron { flex: none; }
  .tab-bar {
    position: absolute; left: 0; right: 0; bottom: 0; height: 118px;
    background: var(--card); border-radius: 70px 70px 0 0;
    display: flex; justify-content: center; gap: 88px; align-items: center;
    padding-bottom: 6px; z-index: 2;
  }
</style>
</head>
<body>
  <svg class="backdrop" width="677" height="1200" viewBox="0 0 677 1200" aria-hidden="true">
    <path d="M430 0 C 560 120 677 220 677 320 L 677 640 C 520 760 330 900 160 1200 L 0 1200 L 0 1040 C 200 840 420 690 580 560 C 640 500 640 360 560 250 C 500 160 420 70 370 0 Z" fill="var(--band)"/>
  </svg>

  <div class="status-bar">
    <span class="status-time">9:41</span>
    <span class="status-icons">
      <svg width="24" height="16" viewBox="0 0 24 16"><rect x="0" y="11" width="4" height="5" rx="1" fill="#111"/><rect x="6" y="8" width="4" height="8" rx="1" fill="#111"/><rect x="12" y="4" width="4" height="12" rx="1" fill="#111"/><rect x="18" y="0" width="4" height="16" rx="1" fill="#111"/></svg>
      <svg width="22" height="16" viewBox="0 0 22 16"><path d="M11 15 l3-3.5a4.5 4.5 0 0 0-6 0z M3.5 7.5a11 11 0 0 1 15 0l2-2.2a14 14 0 0 0-19 0z M6.5 10.8a7 7 0 0 1 9 0l2-2.2a10 10 0 0 0-13 0z" fill="#111"/></svg>
      <svg width="34" height="16" viewBox="0 0 34 16"><rect x="0.5" y="0.5" width="29" height="15" rx="4" fill="none" stroke="#111" opacity="0.5"/><rect x="3" y="3" width="24" height="10" rx="2" fill="#111"/><rect x="31" y="5" width="2.5" height="6" rx="1" fill="#111" opacity="0.5"/></svg>
    </span>
  </div>

  <header class="app-header">
    <h1 class="app-title">PaceUp</h1>
    <p class="app-tagline">Ready to prime your brain?</p>
  </header>

  <main class="mode-list">
    <article class="mode-card">
      <div class="mode-icon mode-icon--focus">
        <svg width="78" height="78" viewBox="0 0 64 64" fill="none" stroke="#fff" stroke-width="4" stroke-linecap="round">
          <circle cx="36" cy="36" r="20" fill="#fff" stroke="none"/>
          <path d="M32 8h8M36 8v6M52 18l3-3"/>
          <path d="M36 26v11l7 5" stroke="#F08F49"/>
          <path d="M4 30h10M2 38h10M6 46h8"/>
        </svg>
      </div>
      <div class="mode-text">
        <h2 class="mode-name">Quick Focus</h2>
        <p class="mode-detail">1-min spatial puzzles</p>
      </div>
      <svg class="mode-chevron" width="16" height="24" viewBox="0 0 16 24"><path d="M4 4l8 8-8 8" fill="none" stroke="var(--ink)" stroke-width="3" stroke-linecap="round" stroke-linejoin="round"/></svg>
    </article>

    <article class="mode-card mode-card--active">
      <div class="mode-icon mode-icon--routine">
        <svg width="74" height="74" viewBox="0 0 64 64">
          <rect x="6" y="10" width="46" height="44" rx="8" fill="#fff"/>
          <rect x="14" y="4" width="5" height="12" rx="2.5" fill="#fff"/>
          <rect x="39" y="4" width="5" height="12" rx="2.5" fill="#fff"/>
          <rect x="6" y="20" width="46" height="3" fill="#FFC000"/>
          <g fill="#FFC000"><rect x="14" y="29" width="6" height="6" rx="1"/><rect x="26" y="29" width="6" height="6" rx="1"/><rect x="14" y="40" width="6" height="6" rx="1"/></g>
          <circle cx="48" cy="48" r="12" fill="#FFC000" stroke="#fff" stroke-width="3"/>
          <path d="M42.5 48l4 4 7-7" fill="none" stroke="#fff" stroke-width="3.2" stroke-linecap="round" stroke-linejoin="round"/>
        </svg>
      </div>
      <div class="mode-text">
        <h2 class="mode-name">Daily Routine</h2>
        <p class="mode-detail">Memory &amp; Word Training</p>
      </div>
      <svg class="mode-chevron" width="16" height="24" viewBox="0 0 16 24"><path d="M4 4l8 8-8 8" fill="none" stroke="var(--ink)" stroke-width="3" stroke-linecap="round" stroke-linejoin="round"/></svg>
    </article>

    <article class="mode-card">
      <div class="mode-icon mode-icon--calm">
        <svg width="80" height="80" viewBox="0 0 64 64" fill="none" stroke="#fff" stroke-width="3.2" stroke-linejoin="round">
          <path d="M32 12c7 7 8 19 0 30c-8-11-7-23 0-30z"/>
          <path d="M32 42c-3-10 0-20 10-24c2 10-2 20-10 24z"/>
          <path d="M32 42c3-10 0-20-10-24c-2 10 2 20 10 24z"/>
          <path d="M32 44c6-6 16-10 26-8c-4 8-14 12-26 8z"/>
          <path d="M32 44c-6-6-16-10-26-8c4 8 14 12 26 8z"/>
        </svg>
      </div>
      <div class="mode-text">
        <h2 class="mode-name">Calming</h2>
        <p class="mode-detail">Sensory &amp; Regulation</p>
      </div>
      <svg class="mode-chevron" width="16" height="24" viewBox="0 0 16 24"><path d="M4 4l8 8-8 8" fill="none" stroke="var(--ink)" stroke-width="3" stroke-linecap="round" stroke-linejoin="round"/></svg>
    </article>
  </main>

  <nav class="tab-bar" aria-label="Main navigation">
    <svg width="50" height="50" viewBox="0 0 64 64" fill="var(--nav-icon)" stroke="var(--nav-icon)" stroke-width="4" stroke-linecap="round">
      <circle cx="36" cy="36" r="20" stroke="none"/>
      <path d="M32 8h8M36 8v6M52 18l3-3" fill="none"/>
      <path d="M36 26v11l7 5" fill="none" stroke="#fff"/>
      <path d="M4 30h10M2 38h10M6 46h8" fill="none"/>
    </svg>
    <svg width="48" height="48" viewBox="0 0 64 64">
      <rect x="6" y="10" width="46" height="44" rx="8" fill="var(--nav-icon)"/>
      <rect x="14" y="4" width="5" height="12" rx="2.5" fill="var(--nav-icon)"/>
      <rect x="39" y="4" width="5" height="12" rx="2.5" fill="var(--nav-icon)"/>
      <rect x="6" y="20" width="46" height="3" fill="#fff"/>
      <g fill="#fff"><rect x="14" y="29" width="6" height="6" rx="1"/><rect x="26" y="29" width="6" height="6" rx="1"/><rect x="14" y="40" width="6" height="6" rx="1"/></g>
      <circle cx="48" cy="48" r="12" fill="var(--nav-icon)" stroke="#fff" stroke-width="3"/>
      <path d="M42.5 48l4 4 7-7" fill="none" stroke="#fff" stroke-width="3.2" stroke-linecap="round" stroke-linejoin="round"/>
    </svg>
    <svg width="54" height="54" viewBox="0 0 64 64" fill="var(--nav-icon)" stroke="#fff" stroke-width="1.6" stroke-linejoin="round">
      <path d="M32 44c6-6 16-10 26-8c-4 8-14 12-26 8z"/>
      <path d="M32 44c-6-6-16-10-26-8c4 8 14 12 26 8z"/>
      <path d="M32 42c-3-10 0-20 10-24c2 10-2 20-10 24z"/>
      <path d="M32 42c3-10 0-20-10-24c-2 10 2 20 10 24z"/>
      <path d="M32 12c7 7 8 19 0 30c-8-11-7-23 0-30z"/>
    </svg>
    <svg width="46" height="46" viewBox="0 0 64 64">
      <g fill="var(--nav-icon)">
        <circle cx="32" cy="32" r="20"/>
        <g>
          <rect x="27" y="4" width="10" height="12" rx="2"/>
          <rect x="27" y="48" width="10" height="12" rx="2"/>
          <rect x="4" y="27" width="12" height="10" rx="2"/>
          <rect x="48" y="27" width="12" height="10" rx="2"/>
          <rect x="27" y="4" width="10" height="12" rx="2" transform="rotate(45 32 32)"/>
          <rect x="27" y="48" width="10" height="12" rx="2" transform="rotate(45 32 32)"/>
          <rect x="4" y="27" width="12" height="10" rx="2" transform="rotate(45 32 32)"/>
          <rect x="48" y="27" width="12" height="10" rx="2" transform="rotate(45 32 32)"/>
        </g>
      </g>
      <circle cx="32" cy="32" r="8" fill="#fff"/>
    </svg>
  </nav>
</body>
</html>
```